Vortane Labs - Methylene Blue Product Packaging

Our brand is Vortane Labs. We are launching a new product that is Methylene Blue, you can see more about this product if you search on Brisko or Pelludo and you will see what it is. This will be for a 50ml bottle. Give me different options for packaging that is minimalist and clean for this brand that makes it look well made and make people want to buy. I've added examples of what the bottle shape will be and potential packaging shapes so you can make packaging on those based off of that.

```html
<!DOCTYPE html>
<html lang="en">
<head>
<meta charset="utf-8">
<title>Vortane Labs – Methylene Blue label sheet</title>
<link rel="stylesheet" href="https://fonts.googleapis.com/css2?family=Montserrat:wght@400;500;600;700;900&display=swap">
<style>
  :root {
    --brand-blue: #0085CA;
    --pattern-blue: #0a89cc;
    --pattern-light: #3aa3da;
    --ink: #000000;
    --paper: #ffffff;
    --label-text: #ffffff;
  }
  * { margin: 0; padding: 0; box-sizing: border-box; }
  html, body { width: 1100px; height: 1200px; overflow: hidden; background: var(--paper); }
  body { font-family: "Montserrat", Arial, sans-serif; color: var(--ink); }
  .sheet { position: relative; width: 1100px; height: 1200px; }
  .mockup { position: absolute; display: block; }
  .mockup--wrapped { left: 101px; top: 107px; width: 433px; height: 287px; }
  .mockup--pattern { left: 557px; top: 107px; width: 433px; height: 287px; }
  .mockup--label { left: 97px; top: 456px; width: 433px; height: 163px; }
  .caption {
    position: absolute; font-family: "Montserrat", Arial, sans-serif;
    font-weight: 900; font-size: 20px; line-height: 1; color: var(--ink);
  }
  .caption--pattern { right: 110px; top: 400px; }
  .caption--label { left: 97px; top: 634px; }
  .caption--background { left: 670px; top: 596px; }
  .swatch { position: absolute; left: 604px; top: 553px; width: 43px; height: 43px; background: var(--brand-blue); }
  .swatch-code { position: absolute; left: 604px; top: 603px; font-size: 12px; font-weight: 400; letter-spacing: 0.2px; }
  .designer-note {
    position: absolute; left: 105px; top: 826px; width: 860px;
    font-size: 19.5px; line-height: 24.5px; font-weight: 400; letter-spacing: 0.35px; text-align: justify;
  }
  .label-text { fill: var(--label-text); font-family: "Montserrat", Arial, sans-serif; }
</style>
</head>
<body>
<main class="sheet">

  <svg class="mockup mockup--wrapped" viewBox="0 0 433 287" aria-label="Label wrapped over patterned background">
    <rect width="433" height="287" fill="var(--brand-blue)"/>
    <g role="img" aria-label="Decorative hexagon molecule pattern band">
      <rect x="0" y="0" width="433" height="81" fill="var(--pattern-blue)"/>
    </g>
    <g role="img" aria-label="Decorative hexagon molecule pattern band">
      <rect x="0" y="244" width="433" height="43" fill="var(--pattern-blue)"/>
    </g>
    <g transform="translate(0 81)">
      <use href="#label-artwork"/>
    </g>
  </svg>

  <svg class="mockup mockup--pattern" viewBox="0 0 433 287" role="img" aria-label="Background pattern: white hexagon molecule lines on blue">
    <defs>
      <linearGradient id="pattern-tone" x1="0" y1="0" x2="1" y2="1">
        <stop offset="0" stop-color="var(--pattern-blue)"/>
        <stop offset="1" stop-color="var(--pattern-light)"/>
      </linearGradient>
    </defs>
    <rect width="433" height="287" fill="url(#pattern-tone)"/>
  </svg>
  <p class="caption caption--pattern">pattern</p>

  <svg class="mockup mockup--label" viewBox="0 0 433 163" aria-label="Blue product label with texts and brand name">
    <defs>
      <g id="label-artwork">
        <rect width="433" height="163" fill="var(--brand-blue)"/>
        <text class="label-text" font-weight="700" font-size="29" transform="translate(222 123) rotate(-90)" textLength="104" lengthAdjust="spacingAndGlyphs">Vortane</text>
        <text class="label-text" font-weight="700" font-size="15" transform="translate(236 57) rotate(-90)" textLength="38" lengthAdjust="spacingAndGlyphs">Labs</text>
        <text class="label-text" font-weight="500" font-size="8.6" x="213" y="139" text-anchor="middle">Methylene Blue</text>
        <text class="label-text" font-weight="400" font-size="5.6" x="214" y="150" text-anchor="middle">50ml</text>
        <rect x="359" y="39" width="20" height="104" fill="none" stroke="var(--label-text)" stroke-width="1"/>
        <g class="label-text" font-size="2.6" font-weight="400">
          <text transform="translate(365 138) rotate(-90)">Read the leaflet before use. Shake well before</text>
          <text transform="translate(369 138) rotate(-90)">each use. Store below 25°C away from light.</text>
          <text transform="translate(373 138) rotate(-90)">Use within six months of opening.</text>
        </g>
        <g class="label-text" font-size="2.6" font-weight="400">
          <text font-weight="600" transform="translate(40 150) rotate(-90)">MANUFACTURER</text>
          <text transform="translate(44 150) rotate(-90)">Made by Vortane Labs, store cool and dry,</text>
          <text transform="translate(48 150) rotate(-90)">keep out of reach of children.</text>
          <text transform="translate(60 70) rotate(-90)">Batch code: 12345</text>
          <text transform="translate(64 70) rotate(-90)">manufacturing date 06/07/2024</text>
        </g>
        <circle cx="60" cy="88" r="6" fill="none" stroke="var(--label-text)" stroke-width="1.4"/>
      </g>
    </defs>
    <use href="#label-artwork"/>
  </svg>
  <p class="caption caption--label">label</p>

  <div class="swatch" aria-hidden="true"></div>
  <p class="swatch-code">#0085CA</p>
  <p class="caption caption--background">background pattern</p>

  <p class="designer-note">
    To wrap a graphic on a thermostatic bottle you should have the print guide file and the exact measurements of the bottle.<br>
    The label projects I made are composed of two elements: the background pattern with a blue background + blue label with texts/logo.<br>
    The render and the bottle were made with Rhombix 3D modeling software, so during the render phase I used the decal function to have the wrapping effect you wanted, the label is in a white and blue version. I remain waiting<br>
    Best regards
  </p>

</main>
</body>
</html>
```